Banner Ad Design Project

I require banner ad designs with the below wording.

1. Join Today and Make Money Tomorrow. Unlimited Income. Click Here Now

2. I lost my job. Now I Make Over $5,000 Per Week From Home. You Can Too. Free Info, Apply Now

I require sizes: 300x250 and 728x90 and 468x60 and 120x240

The design should communicate legitimate, accredited, online business.

Industry/Entity Type

Business

Requirements
Should not have
• Creative attributes to avoid*
Phone numbers in creative
Creative with no click buttons
Interactive creative
Brand messaging with no call to action
Creative with long looping times

```html
<!DOCTYPE html>
<html lang="en">
<head>
<meta charset="utf-8">
<title>Join Today Banner</title>
<link href="https://fonts.googleapis.com/css2?family=Tinos:wght@700&display=swap" rel="stylesheet">
<style>
  :root {
    --canvas: #ffffff;
    --band-light: #f1f7eb;
    --band-mid: #dcebcf;
    --band-deep: #c3dcae;
    --ink: #1c5417;
    --glow: #eef9e4;
    --money-light: #eef3ea;
    --money-mid: #c9d9c0;
    --money-deep: #9fbb95;
    --dollar-deep: #4c7a45;
    --dollar-mid: #9cbf92;
  }
  * { margin: 0; padding: 0; box-sizing: border-box; }
  html, body {
    width: 1200px;
    height: 148px;
    overflow: hidden;
    background: var(--canvas);
  }
  .banner {
    position: relative;
    width: 1200px;
    height: 148px;
    overflow: hidden;
    background: linear-gradient(90deg,
      var(--canvas) 0%,
      var(--band-light) 16%,
      var(--band-mid) 45%,
      var(--band-deep) 66%,
      var(--band-light) 76%,
      var(--canvas) 86%);
  }
  .dollar-art {
    position: absolute;
    left: 0;
    top: 0;
    width: 185px;
    height: 148px;
    background:
      linear-gradient(155deg, rgba(255,255,255,0) 30%, rgba(156,191,146,0.35) 55%, rgba(255,255,255,0) 80%),
      linear-gradient(90deg, var(--dollar-mid) 0%, var(--money-light) 45%, rgba(255,255,255,0) 100%);
  }
  .houses-art {
    position: absolute;
    left: 880px;
    top: 22px;
    width: 320px;
    height: 112px;
    background:
      linear-gradient(180deg, rgba(255,255,255,0) 0%, rgba(201,217,192,0.7) 35%, var(--money-mid) 70%, rgba(255,255,255,0) 100%),
      linear-gradient(90deg, rgba(255,255,255,0) 0%, var(--money-deep) 70%, var(--money-mid) 100%);
    opacity: 0.85;
  }
  .headline {
    position: absolute;
    left: 205px;
    width: 700px;
    top: 38px;
    text-align: center;
    font-family: "Tinos", "Times New Roman", serif;
    font-weight: 700;
    font-size: 32px;
    line-height: 40px;
    color: var(--ink);
    text-shadow: 0 0 2px var(--glow), 0 0 4px var(--glow), 0 0 7px var(--glow), 1px 2px 2px rgba(0,0,0,0.35);
  }
  .headline span { display: block; white-space: nowrap; }
  .headline .cta-link {
    display: inline;
    color: inherit;
    text-decoration: none;
    cursor: pointer;
  }
</style>
</head>
<body>
  <a class="banner" href="#apply" style="display:block">
    <div class="dollar-art" role="img" aria-label="Large tilted green dollar sign casting a soft shadow"></div>
    <div class="headline">
      <span>Join Today and Make Money Tomorrow.</span>
      <span>Unlimited Income. <span class="cta-link">Click Here Now</span></span>
    </div>
    <div class="houses-art" role="img" aria-label="Row of small houses folded from dollar bills"></div>
  </a>
</body>
</html>
```